Most captivating card ever!

Life Coach - Professional Adventurer - Entrepreneur
I need the worlds most amazing business card for my personal brand. This business card will mostly be used to give to prospective clients for life coaching and business coaching.
Be creative, be adventurous. It needs to stand out. Make people say.. I need this guy!
My background is as an entrepreneur and professional adventurer undertaking extreme expeditions. I am now moving into life coaching.
No specific design ideas, so you have full creativity. Show me your best.
Industry/Entity Type
Life Coaching
Contact Information for Business Card
Dan Pellow
itsdanp.com.au
0468215903
Colors
Designer to choose colors to be used in the design.
Look and feel

```html
<!DOCTYPE html>
<html lang="en">
<head>
<meta charset="utf-8">
<title>Dan Pellow – Business Card</title>
<link rel="stylesheet" href="https://fonts.googleapis.com/css2?family=Open+Sans:wght@600;700;800&display=swap">
<style>
  :root {
    --backdrop: #fdfdd2;
    --card-yellow: #eaea00;
    --card-yellow-shade: #d4d400;
    --card-black: #000000;
    --text-white: #ffffff;
  }
  * { margin: 0; padding: 0; box-sizing: border-box; }
  html, body { width: 1200px; height: 1000px; overflow: hidden; }
  body {
    background: radial-gradient(ellipse at center, #fffff0 0%, var(--backdrop) 70%);
    font-family: "Open Sans", Arial, sans-serif;
    position: relative;
  }
  .card {
    position: absolute;
    left: 210px;
    width: 780px;
    overflow: hidden;
  }
  .card--front { top: 41px; height: 446px; background: var(--card-yellow); }
  .card--back { top: 514px; height: 444px; background: var(--card-black); }

  .card__shapes { position: absolute; inset: 0; }
  .shape-black { fill: var(--card-black); }

  .watermark {
    position: absolute;
    font-weight: 800;
    color: var(--card-yellow-shade);
    white-space: nowrap;
    line-height: 1;
  }
  .watermark--life { left: 80px; top: 345px; font-size: 84px; }
  .watermark--upside { left: -10px; top: 240px; font-size: 72px; transform: rotate(180deg); }
  .watermark--top { left: -10px; top: 20px; font-size: 64px; transform: rotate(180deg); }
  .watermark--mid { left: 510px; top: 258px; font-size: 66px; }

  .brand {
    position: absolute;
    transform-origin: left bottom;
    white-space: nowrap;
  }
  .brand__name {
    font-weight: 700;
    color: var(--card-yellow);
    line-height: 1;
  }
  .brand__tagline {
    font-weight: 700;
    color: var(--text-white);
    line-height: 1;
  }
  .brand--front { left: 150px; top: 72px; transform: rotate(-9.5deg); }
  .brand--front .brand__name { font-size: 60px; }
  .brand--front .brand__tagline { font-size: 19px; margin-top: 12px; margin-left: 16px; }

  .brand--back { left: 48px; top: 170px; }
  .brand--back .brand__name { font-size: 64px; }
  .brand--back .brand__tagline { font-size: 22px; margin-top: 16px; margin-left: 10px; }

  .brand-dot {
    position: absolute;
    border-radius: 50%;
    background: var(--card-yellow);
  }
  .brand-dot--front { left: 688px; top: 126px; width: 34px; height: 34px; }
  .brand-dot--back { left: 652px; top: 92px; width: 44px; height: 44px; }

  .contact {
    position: absolute;
    left: 82px;
    top: 360px;
    font-weight: 700;
    font-size: 23px;
    line-height: 31px;
    color: var(--card-black);
  }
</style>
</head>
<body>
  <section class="card card--front">
    <span class="watermark watermark--top">Coach</span>
    <span class="watermark watermark--upside">Coach</span>
    <span class="watermark watermark--mid">Life Coa</span>
    <span class="watermark watermark--life">Life Coach</span>

    <svg class="card__shapes" width="780" height="446" viewBox="0 0 780 446" aria-hidden="true">
      <polygon class="shape-black" points="103,0 780,0 780,446 578,446 752,223 188,319"/>
    </svg>

    <div class="brand brand--front">
      <div class="brand__name">Dan Pellow</div>
      <div class="brand__tagline">Life Coach - Professional Adventurer - Entrepreneur</div>
    </div>
    <span class="brand-dot brand-dot--front"></span>

    <div class="contact">
      <div class="contact__web">itsdanp.com.au</div>
      <div class="contact__phone">0468215903</div>
    </div>
  </section>

  <section class="card card--back">
    <div class="brand brand--back">
      <div class="brand__name">Dan Pellow</div>
      <div class="brand__tagline">Life Coach - Professional Adventurer - Entrepreneur</div>
    </div>
    <span class="brand-dot brand-dot--back"></span>
  </section>
</body>
</html>
```